Real estate investor business card to retire young ;)!

I need a logo design and a business card. I am based in Montreal, Canada. I buy multi-family properties and do lots development. The final design should communicate that I am a problem solver and reliable.

This card will be given to other investors, to potential sellers and industry experts.

Target Market(s)

Real estate community, multi-family owners

Industry/Entity Type

Real Estate Development

Contact Information for Business Card

My name: Lorane Vatelic
email: immo.lorane.vatelic@postbrume.com
cellphone: (555) 274-3916

Logo Text

Gestion immobilière

Font styles to use
Sans Serif

Colors
3176b5

Requirements
Must have
• Within 1-2 seconds the person who sees my card should know that I buy properties and lot. Areas to for Phone number and email adress. I do not have a business name. The card should simply state my name and what I do. The logo should be remembered by the person who reads my card
Should not have
• Colors too bright. Too much small details. I want something balanced, bold without being agressive.

```html
<!DOCTYPE html>
<html lang="en">
<head>
<meta charset="utf-8">
<title>Lorane Vatelic — Business Card</title>
<link rel="stylesheet" href="https://fonts.googleapis.com/css2?family=Alegreya+Sans+SC:wght@400;500&family=Source+Sans+3:wght@400&display=swap">
<style>
  :root {
    --backdrop: #001a30;
    --card: #0066a0;
    --ink: #ffffff;
    --echo-strong: rgba(190, 205, 230, 0.42);
    --echo-soft: rgba(140, 170, 210, 0.10);
  }
  * { margin: 0; padding: 0; box-sizing: border-box; }
  html, body {
    width: 1200px;
    height: 960px;
    overflow: hidden;
    background: var(--backdrop);
  }
  .canvas {
    position: relative;
    width: 1200px;
    height: 960px;
  }
  .card {
    position: absolute;
    left: 261px;
    width: 703px;
    height: 367px;
    background: var(--card);
    overflow: hidden;
  }
  .card--front { top: 103px; }
  .card--back { top: 510px; height: 368px; }

  .name {
    position: absolute;
    font-family: "Alegreya Sans SC", "Source Sans 3", sans-serif;
    font-weight: 500;
    line-height: 1;
    white-space: nowrap;
  }
  .name--front {
    left: 0;
    right: 0;
    top: 173px;
    text-align: center;
    font-size: 46px;
    letter-spacing: 0.28em;
    padding-left: 0.28em;
    color: var(--ink);
  }
  .name--echo-1 {
    left: 31px;
    top: 55px;
    font-size: 50px;
    letter-spacing: 0.28em;
    color: var(--echo-strong);
  }
  .name--echo-2 {
    left: 75px;
    top: 143px;
    font-size: 29px;
    letter-spacing: 0.26em;
    color: var(--echo-soft);
  }
  .name--echo-3 {
    left: 117px;
    top: 245px;
    font-size: 50px;
    letter-spacing: 0.28em;
    color: var(--echo-soft);
  }
  .name--echo-4 {
    right: 30px;
    top: 308px;
    font-size: 31px;
    letter-spacing: 0.28em;
    margin-right: -0.28em;
    color: var(--echo-strong);
  }

  .contact {
    position: absolute;
    right: 30px;
    font-family: "Source Sans 3", sans-serif;
    font-weight: 400;
    color: var(--ink);
    line-height: 1;
    white-space: nowrap;
  }
  .contact--phone {
    top: 149px;
    font-size: 28px;
    letter-spacing: 0.18em;
    margin-right: -0.18em;
  }
  .contact--email {
    top: 198px;
    font-size: 15px;
    letter-spacing: 0.26em;
    margin-right: -0.26em;
  }
</style>
</head>
<body>
  <main class="canvas">
    <section class="card card--front" aria-label="Card front">
      <h1 class="name name--front">Lorane Vatelic</h1>
    </section>

    <section class="card card--back" aria-label="Card back">
      <p class="name name--echo-1" aria-hidden="true">Lorane Vatelic</p>
      <p class="name name--echo-2" aria-hidden="true">Lorane Vatelic</p>
      <p class="name name--echo-3" aria-hidden="true">Lorane Vatelic</p>
      <p class="name name--echo-4">Lorane Vatelic</p>
      <p class="contact contact--phone">(555) 274-3916</p>
      <p class="contact contact--email">immo.lorane.vatelic@postbrume.com</p>
    </section>
  </main>
</body>
</html>
```